Harborline Telecom Print Ad

I'm looking for a four panel piece for Harborline Telecom similar to the attached ad for QuietEar that is a clean, not too busy look using the elements from Harborline Telecom's website:

https://www.harborlinetelecom.example/

We like to include impactful imagery on the cover, more details on the service like a quote from their Founder, a "How it works" section, and other simple icons to communicate Harborline Telecom's benefits in the middle two panels, and testimonials on the back.

Here are a few other 4 panel creative examples for creative inspiration:

https://pages.leafviewer.example/view/471903586/

```html
<!DOCTYPE html>
<html lang="en">
<head>
<meta charset="utf-8">
<title>Harborline Telecom – Four Panel Brochure</title>
<link href="https://fonts.googleapis.com/css2?family=Montserrat:ital,wght@0,400;0,500;0,600;0,700;1,400&display=swap" rel="stylesheet">
<style>
:root{
  --stage:#e4e5e8;
  --paper:#ffffff;
  --navy:#121a2c;
  --ink:#1d2433;
  --muted:#4a5262;
  --sky:#5cc3e7;
  --sky-soft:#a9dff2;
  --sky-pale:#d3f0fb;
  --violet:#8482c8;
  --lavender:#aaa9dd;
  --highlight:#ffe94a;
  --partner:#7a8798;
}
*{box-sizing:border-box;margin:0;padding:0}
html,body{width:1200px;height:3844px;overflow:hidden}
body{background:var(--stage);font-family:"Montserrat",Arial,sans-serif;color:var(--ink);position:relative}
.sheet{position:absolute;background:var(--paper);overflow:hidden;box-shadow:0 6px 24px rgba(20,30,50,.12)}
.sheet *{position:absolute}
.cover-sheet{--u:2.7px;left:200px;top:90px;width:calc(296*var(--u));height:calc(455*var(--u))}
.outside-spread{--u:1.926px;left:30px;top:1430px;width:calc(592*var(--u));height:calc(455*var(--u))}
.inside-spread{--u:1.926px;left:30px;top:2480px;width:calc(592*var(--u));height:calc(455*var(--u))}
.fold{top:0;bottom:0;width:1px;left:calc(296*var(--u));background:rgba(0,0,0,.05)}

/* photo placeholders */
.photo-man{background:linear-gradient(165deg,#d4cfc3 0%,#a6a396 30%,#6f7c78 55%,#3e5762 78%,#2b3c45 100%)}
.photo-woman{background:linear-gradient(150deg,#f1eee8 0%,#d9d3cb 45%,#b9c3cc 75%,#8fa3b2 100%)}
.illustration-strip{background:linear-gradient(180deg,rgba(255,255,255,0) 0%,#eef7fb 45%,#dcf0f8 100%)}
.device-art{background:radial-gradient(ellipse at 50% 60%,#4a4f5a 0%,#2a2e36 55%,rgba(42,46,54,0) 72%)}

/* front cover */
.front{top:0;width:calc(296*var(--u));height:calc(455*var(--u))}
.call-pill{right:0;top:calc(8*var(--u));width:calc(172*var(--u));height:calc(15*var(--u));background:var(--sky-soft);color:#fff;display:flex;align-items:center;justify-content:flex-end;gap:calc(5*var(--u));padding-right:calc(8*var(--u));font-size:calc(4.6*var(--u))}
.call-pill *{position:static}
.call-pill b{font-size:calc(8*var(--u));font-weight:600}
.brand{right:calc(18*var(--u));top:calc(86*var(--u));display:flex;align-items:center;gap:calc(4*var(--u));font-size:calc(13.5*var(--u));font-weight:600;color:var(--navy);white-space:nowrap}
.brand *{position:static}
.brand i{width:calc(5*var(--u));height:calc(5*var(--u));border-radius:50%;background:var(--sky);display:block}
.headline{left:calc(14*var(--u));top:calc(316*var(--u));display:flex;flex-direction:column;align-items:flex-start;gap:calc(2*var(--u))}
.headline span{position:static;background:var(--sky);color:var(--navy);font-weight:700;font-size:calc(17*var(--u));line-height:1.1;padding:0 calc(3*var(--u));letter-spacing:.02em}
.tagline{left:calc(14*var(--u));top:calc(404*var(--u));width:calc(240*var(--u));color:#fff;font-size:calc(9.4*var(--u));line-height:1.3}

/* back panel */
.trusted{left:0;width:calc(296*var(--u));top:calc(26*var(--u));text-align:center;font-size:calc(8.4*var(--u));font-weight:500;line-height:1.3;color:var(--navy)}
.partners{left:calc(18*var(--u));top:calc(63*var(--u));width:calc(264*var(--u));display:flex;justify-content:space-between;align-items:center}
.partners span{position:static;font-size:calc(5.6*var(--u));font-weight:700;color:var(--partner);white-space:nowrap;text-transform:uppercase}
.love-box{left:0;top:calc(128*var(--u));width:calc(214*var(--u));height:calc(212*var(--u));background:var(--sky);padding:calc(16*var(--u)) calc(22*var(--u))}
.love-box *{position:static}
.love-box h2{font-size:calc(10.6*var(--u));font-weight:600;color:var(--navy);margin-bottom:calc(10*var(--u))}
.love-box p{font-size:calc(4.9*var(--u));line-height:1.35;color:var(--navy);margin-bottom:calc(9*var(--u))}
.love-box h3{font-size:calc(5.6*var(--u));font-weight:600;color:var(--navy);margin-bottom:calc(3*var(--u))}
.love-box .quote{font-style:italic}
.get-service{left:calc(22*var(--u));top:calc(356*var(--u));width:calc(150*var(--u))}
.get-service *{position:static}
.get-service h2{font-size:calc(9*var(--u));font-weight:500;line-height:1.1;color:var(--navy);margin-bottom:calc(6*var(--u))}
.get-service p{font-size:calc(4.8*var(--u));color:var(--muted);line-height:1.4}
.get-service .phone{font-size:calc(9*var(--u));font-weight:600;color:var(--navy);margin:calc(2*var(--u)) 0 calc(4*var(--u))}

/* inside left */
.offer-banner{left:0;top:0;width:calc(296*var(--u));height:calc(33*var(--u));background:var(--violet);color:#fff;font-size:calc(7.2*var(--u));text-align:center;line-height:1.3;padding:calc(4*var(--u)) calc(30*var(--u)) 0}
.offer-banner *{position:static}
.offer-banner mark{background:var(--highlight);color:var(--navy);font-weight:600;padding:0 calc(1*var(--u))}
.why-title{left:0;width:calc(296*var(--u));top:calc(42*var(--u));text-align:center;font-size:calc(9.5*var(--u));font-weight:500;color:var(--navy)}
.benefit{width:calc(120*var(--u))}
.benefit *{position:static}
.benefit h4{font-size:calc(5.6*var(--u));font-weight:600;color:var(--navy);margin-bottom:calc(1.5*var(--u));line-height:1.2}
.benefit p{font-size:calc(4.7*var(--u));line-height:1.3;color:var(--muted)}
.info-box{left:calc(172*var(--u));top:calc(210*var(--u));width:calc(124*var(--u));height:calc(145*var(--u));background:var(--lavender);padding:calc(10*var(--u)) calc(9*var(--u))}
.info-box *{position:static}
.info-box h3{font-size:calc(9*var(--u));font-weight:500;color:var(--navy);line-height:1.1;margin-bottom:calc(3*var(--u))}
.info-box p{font-size:calc(4.6*var(--u));line-height:1.3;color:var(--navy);margin-bottom:calc(8*var(--u))}
.footer-bar{left:0;bottom:0;width:calc(592*var(--u));height:calc(17*var(--u));background:var(--navy);color:#fff;font-size:calc(5.4*var(--u))}
.footer-bar span{top:50%;transform:translateY(-50%);white-space:nowrap}
.footer-bar b{position:static;font-size:calc(7*var(--u));font-weight:600;margin-left:calc(4*var(--u))}

/* inside right */
.safer-title{left:calc(310*var(--u));top:calc(28*var(--u));font-size:calc(8.6*var(--u));font-weight:600;color:var(--navy);line-height:1.15}
.safer-box{left:calc(310*var(--u));top:calc(56*var(--u));width:calc(240*var(--u));height:calc(64*var(--u));background:var(--sky-pale);padding:calc(7*var(--u)) calc(8*var(--u))}
.safer-box ul{position:static;list-style:none}
.safer-box li{position:static;font-size:calc(4.8*var(--u));line-height:1.35;color:var(--muted);width:calc(130*var(--u));padding-left:calc(6*var(--u))}
.safer-box li::before{content:"";position:absolute;left:0;margin-top:calc(2*var(--u));width:calc(2.6*var(--u));height:calc(2.6*var(--u));background:var(--violet)}
.safer-box li{position:relative}
.router{left:calc(448*var(--u));top:calc(30*var(--u));width:calc(132*var(--u));height:calc(100*var(--u))}
.section-label{left:calc(296*var(--u));width:calc(296*var(--u));text-align:center;color:var(--navy);font-weight:500}
.step{top:calc(156*var(--u));width:calc(80*var(--u));height:calc(84*var(--u));text-align:center;padding-top:calc(4*var(--u))}
.step *{position:static}
.step h5{font-size:calc(5.4*var(--u));font-weight:500;color:var(--navy)}
.step .art{display:block;width:calc(40*var(--u));height:calc(36*var(--u));margin:calc(8*var(--u)) auto calc(6*var(--u));border-radius:calc(4*var(--u))}
.step p{font-size:calc(4.4*var(--u));line-height:1.25;color:var(--muted);padding:0 calc(5*var(--u))}
.step-1{left:calc(310*var(--u));background:var(--lavender)}
.step-1 .art{background:linear-gradient(160deg,#3b4a66,#1f2636)}
.step-2{left:calc(393*var(--u));background:var(--sky-soft)}
.step-2 .art{background:linear-gradient(160deg,#ffffff,#c9d3e8)}
.step-3{left:calc(476*var(--u));width:calc(102*var(--u));background:var(--sky-pale)}
.step-3 .art{background:linear-gradient(180deg,#e6f6fc,#a9dff2)}
.plan{top:calc(272*var(--u));width:calc(64*var(--u))}
.plan *{position:static}
.plan .plan-name{display:block;background:var(--navy);color:#fff;text-align:center;font-size:calc(5.4*var(--u));padding:calc(2*var(--u)) 0}
.plan .prices{display:block;background:var(--sky-pale);padding:calc(3*var(--u)) calc(4*var(--u));height:calc(33*var(--u))}
.plan .row{display:flex;align-items:center;gap:calc(3*var(--u));margin-bottom:calc(2*var(--u))}
.plan .amt{font-size:calc(10*var(--u));font-weight:500;color:var(--navy);width:calc(26*var(--u))}
.plan .amt small{font-size:calc(5*var(--u));vertical-align:top}
.plan .row .amt.sub{font-size:calc(8*var(--u))}
.plan .per{font-size:calc(2.8*var(--u));line-height:1.2;color:var(--muted)}
.plan ul{list-style:none;padding:calc(3*var(--u)) calc(3*var(--u)) 0}
.plan li{display:flex;align-items:center;gap:calc(2.5*var(--u));font-size:calc(4.4*var(--u));color:var(--muted);line-height:1.75}
.plan li svg{width:calc(4.5*var(--u));height:calc(4.5*var(--u));flex:none}
</style>
</head>
<body>

<!-- Front cover on its own -->
<section class="sheet cover-sheet" aria-label="Front cover">
  <div class="photo-man" role="img" aria-label="Photo of a smiling older man with a white beard talking on a corded landline phone at home" style="left:0;top:calc(110*var(--u));width:calc(296*var(--u));height:calc(345*var(--u))"></div>
  <div class="front" style="left:0">
    <div class="call-pill"><span>Call our landline specialists</span><b>800-555-0142</b></div>
    <div class="brand"><i></i><span>Harborline Telecom</span></div>
    <div class="headline"><span>SIMPLE,</span><span>RELIABLE,</span><span>PHONE SERVICE</span></div>
    <p class="tagline">Modern landline and wireless phone service that doesn’t require internet.</p>
  </div>
</section>

<!-- Outside spread: back panel + front cover -->
<section class="sheet outside-spread" aria-label="Outside spread">
  <div class="photo-man" role="img" aria-label="Photo of a smiling older man with a white beard talking on a corded landline phone at home" style="left:calc(178*var(--u));top:calc(110*var(--u));width:calc(414*var(--u));height:calc(345*var(--u))"></div>

  <p class="trusted">Trusted in 10,000+ homes and<br>businesses including</p>
  <div class="partners">
    <span>Maple Crumb</span><span>Petrovane</span><span>Stonegate Bank</span><span>Coop &amp; Co</span><span>Bean Harbor</span><span>Fizzmont</span>
  </div>

  <div class="love-box">
    <h2>OUR CUSTOMERS LOVE US</h2>
    <p>Our US-based customer support team is with you every step of the way. Via email or phone, you’ll always reach someone who can answer all of your questions.</p>
    <h3>Marla Benton</h3>
    <p class="quote">If you need to port over your landline and your provider won’t do it for you, then you need this company. It was a smooth transition and my mom now gets to keep her phone number that she has had for over 30 years. Had to move her to an assisted living and being without a phone to all her friends was a BIG concern for me…</p>
    <h3>Cedar Bend Farm</h3>
    <p class="quote">Harborline Telecom offered me a friendly neighborhood phone company equivalent when no other utility was available in my area. The representatives are honest and concise. What they advertise is what you get. No extra plans or fees. The quality is clear and an equal trade off from traditional landline service…</p>
  </div>

  <div class="get-service">
    <h2>GET YOUR LANDLINE<br>SERVICE TODAY</h2>
    <p>Call our landline specialists</p>
    <p class="phone">800-555-0142</p>
    <p>7am - 9pm ET Mon-Fri<br>9am - 9pm ET Sat/Sun</p>
  </div>

  <div class="front" style="left:calc(296*var(--u))">
    <div class="call-pill"><span>Call our landline specialists</span><b>800-555-0142</b></div>
    <div class="brand"><i></i><span>Harborline Telecom</span></div>
    <div class="headline"><span>SIMPLE,</span><span>RELIABLE,</span><span>PHONE SERVICE</span></div>
    <p class="tagline">Modern landline and wireless phone service that doesn’t require internet.</p>
  </div>
</section>

<!-- Inside spread -->
<section class="sheet inside-spread" aria-label="Inside spread">
  <div class="fold"></div>

  <p class="offer-banner">Unlimited nationwide calling from your landline phone, <mark>starting at $39/month.</mark></p>
  <h2 class="why-title">WHY CHOOSE US</h2>

  <div class="benefit" style="left:calc(20*var(--u));top:calc(68*var(--u))"><h4>No internet required</h4><p>Don’t let the strength of your internet connection decide whether you can connect with your loved ones.</p></div>
  <div class="benefit" style="left:calc(156*var(--u));top:calc(68*var(--u))"><h4>Unlimited nationwide calling</h4><p>Stay in touch with loved ones anywhere in the United States with unlimited minutes.</p></div>
  <div class="benefit" style="left:calc(20*var(--u));top:calc(117*var(--u))"><h4>Customer support you can actually reach</h4><p>Helpful, knowledgeable customer support you can reach via chat, email, or phone.</p></div>
  <div class="benefit" style="left:calc(156*var(--u));top:calc(117*var(--u))"><h4>Get a new, local number</h4><p>Or, keep your existing number by transferring it from your current provider.</p></div>
  <div class="benefit" style="left:calc(20*var(--u));top:calc(160*var(--u))"><h4>30-second setup</h4><p>You can set it up yourself — no technician required. All you need is a power outlet.</p></div>
  <div class="benefit" style="left:calc(156*var(--u));top:calc(160*var(--u))"><h4>Works during power outages</h4><p>Backup battery keeps you connected when the power goes out.</p></div>

  <div class="photo-woman" role="img" aria-label="Photo of a smiling older woman with grey hair holding a white landline handset" style="left:0;top:calc(210*var(--u));width:calc(172*var(--u));height:calc(145*var(--u))"></div>
  <div class="info-box">
    <h3>INTERNATIONAL<br>CALLING</h3>
    <p>Call anywhere in the world for a low per-minute rate. Available with any Harborline Telecom account.</p>
    <h3>HOW IT WORKS</h3>
    <p>The Harborline Telecom landline base connects your handset to the cellular network in your area. This provides you with a more reliable connection than a traditional copper wire landline and VoIP alternatives that rely on your internet connection. You can use your existing handset or purchase a new one from us. It’s that simple!</p>
  </div>

  <h3 class="safer-title">YOUR LANDLINE IS SAFER<br>THAN EVER BEFORE.</h3>
  <div class="safer-box">
    <ul>
      <li>Unlimited local &amp; long-distance calling</li>
      <li>Can move wherever they move</li>
      <li>Works with any existing landline phone</li>
      <li>No more hard-to-use cell phones</li>
      <li>Better voice quality than VOIP and more trusted than copper wire landline</li>
    </ul>
  </div>
  <div class="router device-art" role="img" aria-label="Product photo of the dark landline base unit with two antennas"></div>

  <h4 class="section-label" style="top:calc(142*var(--u));font-size:calc(7.4*var(--u))">LANDLINE SETUP IN 2 EASY STEPS</h4>
  <div class="step step-1"><h5>Landline Base</h5><span class="art" role="img" aria-label="Illustration of the landline base unit"></span><p>Plug our landline base into a power outlet</p></div>
  <div class="step step-2"><h5>Landline Phone</h5><span class="art" role="img" aria-label="Illustration of a cordless landline phone"></span><p>Plug a phone into the jack on our landline base</p></div>
  <div class="step step-3"><h5>Local cell towers</h5><span class="art" role="img" aria-label="Illustration of a cell tower sending signal"></span><p>Installation is that easy!</p></div>

  <h4 class="section-label" style="top:calc(256*var(--u));font-size:calc(10*var(--u))">CELL PLANS</h4>

  <div class="plan" style="left:calc(310*var(--u))">
    <span class="plan-name">1 Line</span>
    <div class="prices">
      <div class="row"><span class="amt"><small>$</small>20</span><span class="per">Per month<br>Pay monthly</span></div>
      <div class="row"><span class="amt sub"><small>$</small>18.25</span><span class="per">Per month<br>Pay annually</span></div>
    </div>
    <ul>
      <li><svg viewBox="0 0 10 10"><circle cx="5" cy="5" r="5" fill="#5a6272"/><path d="M2.8 5.2l1.5 1.5 3-3.2" stroke="#fff" stroke-width="1.2" fill="none"/></svg>5G or 4G LTE</li>
      <li><svg viewBox="0 0 10 10"><circle cx="5" cy="5" r="5" fill="#5a6272"/><path d="M2.8 5.2l1.5 1.5 3-3.2" stroke="#fff" stroke-width="1.2" fill="none"/></svg>Unlimited Talk</li>
      <li><svg viewBox="0 0 10 10"><circle cx="5" cy="5" r="5" fill="#5a6272"/><path d="M2.8 5.2l1.5 1.5 3-3.2" stroke="#fff" stroke-width="1.2" fill="none"/></svg>Unlimited Text</li>
    </ul>
  </div>
  <div class="plan" style="left:calc(377*var(--u))">
    <span class="plan-name">1 Line + Data</span>
    <div class="prices">
      <div class="row"><span class="amt"><small>$</small>30</span><span class="per">Per month<br>Pay monthly</span></div>
      <div class="row"><span class="amt sub"><small>$</small>27.50</span><span class="per">Per month<br>Pay annually</span></div>
    </div>
    <ul>
      <li><svg viewBox="0 0 10 10"><circle cx="5" cy="5" r="5" fill="#5a6272"/><path d="M2.8 5.2l1.5 1.5 3-3.2" stroke="#fff" stroke-width="1.2" fill="none"/></svg>5G or 4G LTE</li>
      <li><svg viewBox="0 0 10 10"><circle cx="5" cy="5" r="5" fill="#5a6272"/><path d="M2.8 5.2l1.5 1.5 3-3.2" stroke="#fff" stroke-width="1.2" fill="none"/></svg>Unlimited Talk</li>
      <li><svg viewBox="0 0 10 10"><circle cx="5" cy="5" r="5" fill="#5a6272"/><path d="M2.8 5.2l1.5 1.5 3-3.2" stroke="#fff" stroke-width="1.2" fill="none"/></svg>Unlimited Text</li>
      <li><svg viewBox="0 0 10 10"><circle cx="5" cy="5" r="5" fill="#5a6272"/><path d="M2.8 5.2l1.5 1.5 3-3.2" stroke="#fff" stroke-width="1.2" fill="none"/></svg>2GB Data</li>
    </ul>
  </div>
  <div class="plan" style="left:calc(444*var(--u))">
    <span class="plan-name">2 Lines</span>
    <div class="prices">
      <div class="row"><span class="amt"><small>$</small>40</span><span class="per">Per month<br>Pay monthly</span></div>
      <div class="row"><span class="amt sub"><small>$</small>36.58</span><span class="per">Per month<br>Pay annually</span></div>
    </div>
    <ul>
      <li><svg viewBox="0 0 10 10"><circle cx="5" cy="5" r="5" fill="#5a6272"/><path d="M2.8 5.2l1.5 1.5 3-3.2" stroke="#fff" stroke-width="1.2" fill="none"/></svg>5G or 4G LTE</li>
      <li><svg viewBox="0 0 10 10"><circle cx="5" cy="5" r="5" fill="#5a6272"/><path d="M2.8 5.2l1.5 1.5 3-3.2" stroke="#fff" stroke-width="1.2" fill="none"/></svg>Unlimited Talk</li>
      <li><svg viewBox="0 0 10 10"><circle cx="5" cy="5" r="5" fill="#5a6272"/><path d="M2.8 5.2l1.5 1.5 3-3.2" stroke="#fff" stroke-width="1.2" fill="none"/></svg>Unlimited Text</li>
    </ul>
  </div>
  <div class="plan" style="left:calc(511*var(--u))">
    <span class="plan-name">2 Lines + Data</span>
    <div class="prices">
      <div class="row"><span class="amt"><small>$</small>50</span><span class="per">Per month<br>Pay monthly</span></div>
      <div class="row"><span class="amt sub"><small>$</small>45.75</span><span class="per">Per month<br>Pay annually</span></div>
    </div>
    <ul>
      <li><svg viewBox="0 0 10 10"><circle cx="5" cy="5" r="5" fill="#5a6272"/><path d="M2.8 5.2l1.5 1.5 3-3.2" stroke="#fff" stroke-width="1.2" fill="none"/></svg>5G or 4G LTE</li>
      <li><svg viewBox="0 0 10 10"><circle cx="5" cy="5" r="5" fill="#5a6272"/><path d="M2.8 5.2l1.5 1.5 3-3.2" stroke="#fff" stroke-width="1.2" fill="none"/></svg>Unlimited Talk</li>
      <li><svg viewBox="0 0 10 10"><circle cx="5" cy="5" r="5" fill="#5a6272"/><path d="M2.8 5.2l1.5 1.5 3-3.2" stroke="#fff" stroke-width="1.2" fill="none"/></svg>Unlimited Text</li>
      <li><svg viewBox="0 0 10 10"><circle cx="5" cy="5" r="5" fill="#5a6272"/><path d="M2.8 5.2l1.5 1.5 3-3.2" stroke="#fff" stroke-width="1.2" fill="none"/></svg>5GB Data</li>
    </ul>
  </div>

  <div class="illustration-strip" role="img" aria-label="Line illustration of a cell tower, signal waves, a landline phone and a woman chatting on the phone among shrubs" style="left:0;top:calc(378*var(--u));width:calc(592*var(--u));height:calc(60*var(--u))"></div>

  <div class="footer-bar">
    <span style="left:calc(312*var(--u))">Need a custom Plan?</span>
    <span style="right:calc(14*var(--u))">Contact us at <b>800-555-0142</b></span>
  </div>
</section>

</body>
</html>
```